we need a business card in yellow, green and black with rounded edges. We are in the Construction and Engineering business. I need the below info included:

Neil Barton
Bluestone Engineering & Construction, Inc.
4168 Harbor Crest Road,
Santa Ana, Ca 92814
714-555-0147 Office
714-555-0192 Cell
714-555-0163 Fax
nb@bluestonexq.example

thanks for your help!

```html
<!DOCTYPE html>
<html lang="en">
<head>
<meta charset="utf-8">
<title>Neil Barton – Business Card</title>
<link rel="stylesheet" href="https://fonts.googleapis.com/css2?family=Saira+Condensed:wght@500&family=Saira:wght@400&family=Lato:wght@400&display=swap">
<style>
  :root {
    --page-bg: #e9e9e6;
    --lime: #b6d43a;
    --lime-light: #dcec9c;
    --lime-deep: #9fc02a;
    --charcoal: #1c1c1c;
    --charcoal-light: #3a3a3a;
    --ink: #0d0d0d;
    --accent-text: #c3dc5a;
  }
  html, body {
    margin: 0;
    padding: 0;
    width: 1200px;
    height: 1000px;
    overflow: hidden;
    background: var(--page-bg);
  }
  .business-card {
    position: absolute;
    left: 150px;
    top: 230px;
    width: 900px;
    height: 540px;
    border-radius: 56px;
    box-shadow: 0 18px 40px rgba(0,0,0,0.25);
  }
  .card-surface {
    position: absolute;
    inset: 0;
    width: 900px;
    height: 540px;
  }
  .holder-name {
    position: absolute;
    left: 88px;
    top: 78px;
    margin: 0;
    font-family: "Saira Condensed", sans-serif;
    font-weight: 500;
    font-size: 80px;
    line-height: 1;
    color: var(--ink);
    letter-spacing: 0.5px;
  }
  .company-name {
    position: absolute;
    left: 88px;
    top: 188px;
    margin: 0;
    font-family: "Saira", sans-serif;
    font-weight: 400;
    font-size: 21px;
    letter-spacing: 2.4px;
    color: var(--ink);
  }
  .contact-list {
    position: absolute;
    left: 80px;
    top: 296px;
    margin: 0;
    padding: 0;
    list-style: none;
    font-family: "Lato", sans-serif;
    font-size: 19px;
    color: var(--accent-text);
  }
  .contact-item {
    display: flex;
    align-items: center;
    height: 40px;
    margin-bottom: 26px;
  }
  .contact-icon {
    width: 40px;
    height: 40px;
    margin-right: 16px;
    flex: none;
  }
  .divider {
    margin: 0 8px;
  }
</style>
</head>
<body>
  <article class="business-card">
    <svg class="card-surface" viewBox="0 0 900 540" aria-hidden="true">
      <defs>
        <clipPath id="card-shape">
          <rect x="0" y="0" width="900" height="540" rx="56" ry="56"/>
        </clipPath>
        <radialGradient id="lime-glow" cx="0.55" cy="0.55" r="0.7">
          <stop offset="0" stop-color="var(--lime-light)"/>
          <stop offset="0.55" stop-color="var(--lime)"/>
          <stop offset="1" stop-color="var(--lime-deep)"/>
        </radialGradient>
        <radialGradient id="charcoal-glow" cx="0.5" cy="0.15" r="0.8">
          <stop offset="0" stop-color="var(--charcoal-light)"/>
          <stop offset="1" stop-color="var(--charcoal)"/>
        </radialGradient>
        <filter id="edge-shadow" x="-10%" y="-20%" width="120%" height="140%">
          <feDropShadow dx="0" dy="-4" stdDeviation="6" flood-color="#000" flood-opacity="0.45"/>
        </filter>
      </defs>
      <g clip-path="url(#card-shape)">
        <rect class="top-band" x="0" y="0" width="900" height="540" fill="url(#lime-glow)"/>
        <path class="bottom-band" filter="url(#edge-shadow)"
              d="M0 292 C 150 262, 330 240, 520 240 C 700 240, 820 252, 900 268 L 900 540 L 0 540 Z"
              fill="url(#charcoal-glow)"/>
      </g>
    </svg>

    <h1 class="holder-name">Neil Barton</h1>
    <p class="company-name">Bluestone Engineering &amp; Construction, Inc.</p>

    <ul class="contact-list">
      <li class="contact-item">
        <svg class="contact-icon" viewBox="0 0 40 40" aria-hidden="true">
          <path d="M20 5 C13 5 9 10 9 16 C9 24 20 35 20 35 C20 35 31 24 31 16 C31 10 27 5 20 5 Z" fill="var(--accent-text)"/>
          <circle cx="20" cy="16" r="4.5" fill="var(--charcoal)"/>
        </svg>
        <span>4168 Harbor Crest Road, Santa Ana, Ca 92814</span>
      </li>
      <li class="contact-item">
        <svg class="contact-icon" viewBox="0 0 40 40" aria-hidden="true">
          <circle cx="20" cy="20" r="19" fill="var(--accent-text)"/>
          <path d="M10 16 C10 12 30 12 30 16 L30 18 L25 18 L25 15.5 L15 15.5 L15 18 L10 18 Z" fill="var(--charcoal)"/>
          <path d="M13 19 L27 19 L29 29 L11 29 Z" fill="var(--charcoal)"/>
          <circle cx="20" cy="24" r="3" fill="var(--accent-text)"/>
        </svg>
        <span>Office: 714-555-0147</span><span class="divider">|</span><span>Cell: 714-555-0192</span><span class="divider">|</span><span>Fax: 714-555-0163</span>
      </li>
      <li class="contact-item">
        <svg class="contact-icon" viewBox="0 0 40 40" aria-hidden="true">
          <circle cx="20" cy="20" r="19" fill="var(--accent-text)"/>
          <rect x="9" y="12" width="22" height="16" fill="var(--charcoal)"/>
          <path d="M9 12 L20 22 L31 12" fill="none" stroke="var(--accent-text)" stroke-width="2"/>
          <path d="M9 28 L17 20 M31 28 L23 20" stroke="var(--accent-text)" stroke-width="1.5"/>
        </svg>
        <span>nb@bluestonexq.example</span>
      </li>
    </ul>
  </article>
</body>
</html>
```